Holiday PROMO Flyer for Healthy Restaurant

Hi ! We need a holiday style promo flyer for Verandel . Please have a holiday vibe type of design in the background. Include at least 1 of the photos that I provide, and our logo of course. This promo is for a new package that we will be offering until December 31st 2022.

It will have a promo of some type of design that says the following in a creative way:
" HOLIDAY PACKAGE PROMO!"
Buy our holiday package of $500 and receive a $100 gift card!" (THIS SHOULD BE VERY NOTICEABLE AS THIS IS THE ACTUAL PROMO)
Our biggest promo to date.
Offer ends December 31st, 2022.

Take a look at our website to stay consistant with the brand as well.

Industry/Entity Type

Restaurant

Requirements
Must have
• Logo, food photo and gift card photo

```html
<!DOCTYPE html>
<html lang="en">
<head>
<meta charset="utf-8">
<title>Verandel Holiday Package Promo</title>
<link href="https://fonts.googleapis.com/css2?family=Oswald:wght@400;500;700&display=swap" rel="stylesheet">
<style>
  :root {
    --backdrop: #7a7a7a;
    --ink-black: #1a1a1a;
    --brand-green: #8dc21f;
    --brand-navy: #0f3464;
    --navy-deep: #0b2a52;
    --wood-light: #e4e7ea;
    --wood-mid: #c9ced3;
    --band-grey: #9a9a9a;
    --accent-orange: #f7a81b;
    --white: #ffffff;
  }
  * { margin: 0; padding: 0; box-sizing: border-box; }
  html, body {
    width: 1200px;
    height: 1200px;
    overflow: hidden;
    background: var(--backdrop);
    font-family: "Oswald", "Arial Narrow", sans-serif;
  }
  .flyer {
    position: absolute;
    left: 195px;
    top: 39px;
    width: 810px;
    height: 1122px;
    overflow: hidden;
    background: var(--wood-light);
  }
  .flyer-shapes { position: absolute; inset: 0; }
  .headline {
    position: absolute;
    left: 58px;
    top: 48px;
    font-weight: 700;
    font-size: 98px;
    line-height: 88px;
    letter-spacing: -1px;
    text-transform: uppercase;
  }
  .headline .green { color: var(--brand-green); display: block; }
  .headline .white { color: var(--white); display: block; font-weight: 500; }
  .brand-name {
    position: absolute;
    left: 410px;
    top: 62px;
    display: flex;
    align-items: center;
    gap: 12px;
    color: var(--brand-green);
    font-weight: 700;
    font-size: 64px;
    letter-spacing: 3px;
    text-transform: uppercase;
  }
  .brand-name .dot {
    width: 18px; height: 18px;
    border-radius: 50%;
    background: var(--brand-green);
  }
  .gift-card {
    position: absolute;
    left: 66px;
    top: 352px;
    width: 290px;
    height: 190px;
    border-radius: 12px;
    background: linear-gradient(135deg, #143d73, var(--navy-deep));
    transform: rotate(-7deg);
    box-shadow: 0 8px 14px rgba(0,0,0,0.35);
  }
  .offer-text {
    position: absolute;
    left: 412px;
    top: 326px;
    width: 340px;
    text-align: center;
    color: var(--brand-navy);
    font-weight: 400;
    font-size: 42px;
    line-height: 44px;
    text-transform: uppercase;
  }
  .offer-text b { font-weight: 700; }
  .closing {
    position: absolute;
    right: 35px;
    top: 1018px;
    text-align: right;
    font-weight: 400;
    font-size: 36px;
    line-height: 43px;
    text-transform: uppercase;
    color: var(--white);
  }
  .closing .ends { color: var(--accent-orange); }
  .closing .date { color: var(--brand-green); }
</style>
</head>
<body>
  <main class="flyer">
    <svg class="flyer-shapes" width="810" height="1122" viewBox="0 0 810 1122">
      <defs>
        <linearGradient id="woodTone" x1="0" y1="0" x2="1" y2="1">
          <stop offset="0" stop-color="#eef0f2"/>
          <stop offset="1" stop-color="#c7ccd1"/>
        </linearGradient>
        <radialGradient id="saladTone" cx="0.45" cy="0.5" r="0.6">
          <stop offset="0" stop-color="#b8682e"/>
          <stop offset="0.55" stop-color="#6fa33a"/>
          <stop offset="1" stop-color="#f2f2ee"/>
        </radialGradient>
        <linearGradient id="burgerTone" x1="0" y1="0" x2="0" y2="1">
          <stop offset="0" stop-color="#d39a5c"/>
          <stop offset="0.45" stop-color="#6fae3a"/>
          <stop offset="0.7" stop-color="#f2c24a"/>
          <stop offset="1" stop-color="#c08a50"/>
        </linearGradient>
        <linearGradient id="navyBand" x1="0" y1="0" x2="1" y2="0">
          <stop offset="0" stop-color="var(--navy-deep)"/>
          <stop offset="1" stop-color="var(--brand-navy)"/>
        </linearGradient>
      </defs>

      <rect class="wood-surface" width="810" height="1122" fill="url(#woodTone)" role="img" aria-label="Light whitewashed wooden table surface"/>

      <path class="grey-band" d="M0 0 H810 V180 C640 350 360 440 0 465 Z" fill="var(--band-grey)"/>
      <path class="black-panel" d="M0 0 H810 V166 C640 335 360 425 0 448 Z" fill="var(--ink-black)"/>

      <ellipse class="salad-photo" cx="255" cy="770" rx="320" ry="268" fill="url(#saladTone)" role="img" aria-label="Grilled chicken salad with arugula, radish, tomato and cucumber on a white plate"/>
      <rect class="burger-photo" x="445" y="628" width="365" height="335" rx="90" fill="url(#burgerTone)" role="img" aria-label="Grilled chicken sandwich with cheese, lettuce and tomato on a sesame bun"/>

      <path class="green-swoosh" d="M810 940 V1122 H200 C300 1020 470 950 810 940 Z" fill="var(--brand-green)"/>
      <path class="navy-band" d="M810 955 V1122 H245 C340 1035 490 965 810 955 Z" fill="url(#navyBand)"/>

      <g class="offer-burst" transform="translate(582 397)" fill="var(--brand-green)">
        <rect x="-131" y="-131" width="262" height="262"/>
        <rect x="-131" y="-131" width="262" height="262" transform="rotate(15)"/>
        <rect x="-131" y="-131" width="262" height="262" transform="rotate(30)"/>
        <rect x="-131" y="-131" width="262" height="262" transform="rotate(45)"/>
        <rect x="-131" y="-131" width="262" height="262" transform="rotate(60)"/>
        <rect x="-131" y="-131" width="262" height="262" transform="rotate(75)"/>
      </g>

      <rect class="trim-line" x="14" y="14" width="782" height="1094" fill="none" stroke="var(--brand-green)" stroke-width="1"/>
    </svg>

    <h1 class="headline">
      <span class="green">Holiday</span>
      <span class="green">Package</span>
      <span class="white">Promo!</span>
    </h1>

    <div class="brand-name"><span class="dot"></span>Verandel</div>

    <div class="gift-card" role="img" aria-label="Navy Verandel gift card wrapped with a green ribbon"></div>

    <p class="offer-text">
      Buy our holiday<br>
      package of <b>$500</b> &amp;<br>
      receive a <b>$100</b><br>
      gift card!
    </p>

    <p class="closing">
      Our biggest promo to date<br>
      <span class="ends">Offer ends</span> <span class="date">December 31st, 2022</span>
    </p>
  </main>
</body>
</html>
```